Business Card Design

Lawyer
Business name "HarlowLaw"
Areas of expertise:
property
commercial
trusts
immigration
franchising
I want the following quote on the back of the card somewhere.
"Education is when you read the fine print,
experience is what you get if you don't." Miles Corbell
Probably the "areas of expertise" should be on the back also to avoid cluttering the front.
As for colours, I like the shades of blue used on qerivo.com.
The basic part of the card with the contact info needs to be white and uncluttered.
Target Market(s)
small to medium sized self employed business people
Industry/Entity Type
Business
Contact Information for Business Card
Dennis Harlow
Phone + 64 9 517 4460
Fax: + 64 9 517 4461
PO Box 742
Kestrel Bay
Marlow 3917
NZ
email: dennis@pinecrestlegal.co.nz

```html
<!DOCTYPE html>
<html lang="en">
<head>
<meta charset="utf-8">
<title>HarlowLaw Business Card</title>
<link href="https://fonts.googleapis.com/css2?family=Open+Sans:wght@300;400;600;700&display=swap" rel="stylesheet">
<style>
  :root {
    --page: #e9ecef;
    --cyan-light: #2fc6e0;
    --cyan: #16a9d2;
    --blue-mid: #1784bf;
    --blue-deep: #135f96;
    --blue-night: #0f4c7c;
    --ink: #ffffff;
    --ink-soft: #e6f5fb;
    --icon-glyph: #1a6fae;
  }
  * { box-sizing: border-box; margin: 0; padding: 0; }
  html, body {
    width: 1200px; height: 902px; overflow: hidden;
    background: var(--page);
    font-family: "Open Sans", Arial, sans-serif;
  }
  .stage {
    position: relative; width: 1200px; height: 902px;
    display: flex; justify-content: center; align-items: center; gap: 80px;
  }
  .card {
    position: relative; width: 380px; height: 622px;
    border-radius: 6px; overflow: hidden; color: var(--ink);
    box-shadow: 0 10px 28px rgba(15, 60, 100, 0.25);
  }
  .card-facets { position: absolute; inset: 0; width: 100%; height: 100%; }
  .card-content { position: relative; height: 100%; }

  /* Back */
  .quote {
    position: absolute; top: 38px; right: 30px; width: 330px;
    text-align: right; font-size: 15px; line-height: 1.35; font-weight: 600;
    color: var(--ink-soft);
  }
  .quote-author { display: block; margin-right: 18px; }
  .firm-name {
    position: absolute; top: 222px; left: 0; right: 0; text-align: center;
    font-size: 40px; font-weight: 700; letter-spacing: 0.5px;
  }
  .expertise-title {
    position: absolute; top: 318px; left: 0; right: 0; text-align: center;
    font-size: 22px; font-weight: 600;
  }
  .expertise-list {
    position: absolute; top: 370px; left: 118px; list-style: none;
    font-size: 22px; font-weight: 600; line-height: 1.3;
  }
  .expertise-list li::before { content: "* "; }

  /* Front */
  .person {
    position: absolute; top: 132px; right: 34px; text-align: right;
  }
  .person-name { font-size: 38px; line-height: 1.1; }
  .person-name .first { font-weight: 300; }
  .person-name .last { font-weight: 700; }
  .person-role { font-size: 24px; font-weight: 700; margin-right: 50px; }
  .contact-list {
    position: absolute; top: 360px; left: 30px; right: 20px; list-style: none;
    font-size: 14px; font-weight: 600;
  }
  .contact-item { display: flex; align-items: center; gap: 12px; height: 40px; white-space: nowrap; }
  .contact-icon {
    width: 26px; height: 26px; border-radius: 50%; background: var(--ink);
    display: flex; align-items: center; justify-content: center; flex: none;
  }
  .contact-icon svg { width: 15px; height: 15px; fill: var(--icon-glyph); }
</style>
</head>
<body>
<main class="stage">

  <section class="card card-back" aria-label="Card back">
    <svg class="card-facets" viewBox="0 0 380 622" preserveAspectRatio="none" aria-hidden="true">
      <defs>
        <linearGradient id="backBase" x1="0" y1="0" x2="0" y2="1">
          <stop offset="0" stop-color="var(--cyan-light)"/>
          <stop offset="0.35" stop-color="var(--cyan)"/>
          <stop offset="0.55" stop-color="var(--blue-mid)"/>
          <stop offset="1" stop-color="var(--blue-night)"/>
        </linearGradient>
      </defs>
      <rect width="380" height="622" fill="url(#backBase)"/>
      <polygon points="0,0 380,0 380,120 0,190" fill="#3dd0e6" opacity="0.35"/>
      <polygon points="0,190 380,120 380,300 0,360" fill="var(--blue-mid)" opacity="0.45"/>
      <polygon points="200,0 380,0 380,300" fill="#ffffff" opacity="0.08"/>
      <polygon points="0,360 380,300 380,622 0,622" fill="var(--blue-deep)" opacity="0.55"/>
      <polygon points="0,420 150,360 0,622" fill="#ffffff" opacity="0.05"/>
    </svg>
    <div class="card-content">
      <p class="quote">"Education is when you read the fine print, experience is what you get if you don't."
        <span class="quote-author">Miles Corbell</span></p>
      <h1 class="firm-name">HarlowLaw</h1>
      <h2 class="expertise-title">"areas of expertise"</h2>
      <ul class="expertise-list">
        <li>Trusts</li>
        <li>Property</li>
        <li>Franchising</li>
        <li>Commercial</li>
        <li>Immigration</li>
      </ul>
    </div>
  </section>

  <section class="card card-front" aria-label="Card front">
    <svg class="card-facets" viewBox="0 0 380 622" preserveAspectRatio="none" aria-hidden="true">
      <defs>
        <linearGradient id="frontBase" x1="0" y1="0" x2="0" y2="1">
          <stop offset="0" stop-color="var(--cyan)"/>
          <stop offset="0.4" stop-color="var(--blue-mid)"/>
          <stop offset="1" stop-color="var(--blue-night)"/>
        </linearGradient>
      </defs>
      <rect width="380" height="622" fill="url(#frontBase)"/>
      <polygon points="0,0 380,0 380,230 0,150" fill="var(--cyan-light)" opacity="0.4"/>
      <polygon points="120,0 380,0 380,230" fill="#ffffff" opacity="0.08"/>
      <polygon points="0,150 380,230 380,320 0,250" fill="var(--blue-mid)" opacity="0.4"/>
      <polygon points="0,250 380,320 380,622 0,622" fill="var(--blue-deep)" opacity="0.5"/>
      <polygon points="200,622 380,480 380,622" fill="#ffffff" opacity="0.06"/>
    </svg>
    <div class="card-content">
      <div class="person">
        <h1 class="person-name"><span class="first">Dennis</span> <span class="last">Harlow</span></h1>
        <p class="person-role">Lawyer</p>
      </div>
      <ul class="contact-list">
        <li class="contact-item">
          <span class="contact-icon"><svg viewBox="0 0 16 16" aria-label="Phone"><path d="M2 5c0-2 2-3 3-3l1 3-1.5 1c.6 2 2.5 3.9 4.5 4.5l1-1.5 3 1c0 1-1 3-3 3C6 13 2 9 2 5z"/></svg></span>
          <span>+ 64 9 517 4460</span>
        </li>
        <li class="contact-item">
          <span class="contact-icon"><svg viewBox="0 0 16 16" aria-label="Fax"><path d="M4 1h8v4H4zM1 6h14v6h-3v3H4v-3H1zM5 10v3h6v-3z"/></svg></span>
          <span>+ 64 9 517 4461</span>
        </li>
        <li class="contact-item">
          <span class="contact-icon"><svg viewBox="0 0 16 16" aria-label="Email"><path d="M1 3h14v1L8 9 1 4zM1 6l7 5 7-5v7H1z"/></svg></span>
          <span>dennis@pinecrestlegal.co.nz</span>
        </li>
        <li class="contact-item">
          <span class="contact-icon"><svg viewBox="0 0 16 16" aria-label="Address"><path d="M8 1l7 6h-2v8h-4v-5H7v5H3V7H1z"/></svg></span>
          <span>PO Box 742 Kestrel Bay Marlow 3917 NZ</span>
        </li>
      </ul>
    </div>
  </section>

</main>
</body>
</html>
```